Retail Label Design - Hand Sanitizer

BRISKEN is Volkmar Norths legacy brand. For decades Volkmar North has been trusted by our customers to provide unmatched capability in the revitalization of surfaces and materials. We are proud to relaunch BRISKENTM with the same promise, but oriented towards a new challenge: meeting the demand for solutions to aid in our collective fight against COVID-19.

BRISKENTM Ethanol Hand Sanitizer is the first official relaunch product – and 80% alcohol based sanitizer, free from fragrance and dye.

We want to maintain a cool and clean feel for the labels – reflective of the product. Ideally if we could incorporate a retro feel to the packaging, we would be very happy.

This label will need to be done to 3 different specs to suit a 235ml, 500ml and 4L package. We would like to start with the 500ml label. I have attached the dieline, (774-QZL) for the 500ml Package. I have also attached product info, logo and brand info.

The only requirements on the front panel is the logo, product name (Ethanol Gel Hand Sanitizer) and the quantity(473ml), space for barcode on back + info provided. the rest we will leave up to your expertise.

Font styles to use
Serif
Sans Serif

Requirements
Must have
• Logo
Product name
Quantity
Information on back panel provided.

```html
<!DOCTYPE html>
<html lang="en">
<head>
<meta charset="utf-8">
<title>BRISKEN Hand Sanitizer Gel – Label Options</title>
<link rel="stylesheet" href="https://fonts.googleapis.com/css2?family=Montserrat:wght@400;500;600;700;800;900&family=Open+Sans:wght@400;700&display=swap">
<style>
  :root{
    --navy:#063b59;
    --orange:#ef8147;
    --teal:#98d5d0;
    --blush:#fdeee6;
    --mist:#dde3e6;
    --white:#ffffff;
    --stage:#d4d4d4;
  }
  *{margin:0;padding:0;box-sizing:border-box}
  html,body{width:720px;height:1200px;overflow:hidden;background:var(--stage)}
  body{position:relative;font-family:"Montserrat",sans-serif;color:var(--navy)}

  .label{position:absolute;left:86px;width:548px;height:368px;background:var(--white);
    box-shadow:3px 4px 6px rgba(0,0,0,.35);overflow:hidden}
  .label--one{top:24px}
  .label--two{top:412px}
  .label--three{top:800px}

  .label-shapes{position:absolute;inset:0;width:548px;height:368px}

  .side-strip{position:absolute;left:0;top:0;width:20px;height:368px;display:flex;align-items:center;justify-content:center}
  .side-strip p{writing-mode:vertical-rl;transform:rotate(180deg);font-size:6.3px;color:var(--white);white-space:nowrap;letter-spacing:.05px}
  .side-strip b{font-weight:700}

  .brand-small{position:absolute;left:103px;top:24px;font-size:17px;font-weight:900;letter-spacing:.5px;color:var(--navy)}
  .brand-large{position:absolute;left:342px;top:56px;font-size:34px;font-weight:900;letter-spacing:1px;color:var(--navy)}

  .info-title{position:absolute;left:30px;top:57px;font-size:6.6px;font-weight:700;white-space:nowrap}
  .info-title span{font-weight:400}
  .info-body{position:absolute;left:30px;top:70px;width:208px;height:180px;overflow:hidden;
    font-family:"Open Sans",sans-serif;font-size:4.05px;line-height:5.55px;text-align:justify}
  .info-body p{margin-bottom:2.6px}
  .info-body b{font-weight:700}

  .warning{position:absolute;left:31px;top:253px;width:205px;height:56px;overflow:hidden;
    font-family:"Open Sans",sans-serif;font-size:4.05px;line-height:5.6px;text-align:justify}
  .warning b{font-weight:700}

  .barcode-space{position:absolute;left:29px;top:315px;width:87px;height:43px;background:var(--white)}
  .maker{position:absolute;left:166px;top:321px;font-family:"Open Sans",sans-serif;font-size:3.9px;color:var(--white)}

  .product{position:absolute;left:299px;width:220px;text-align:center}
  .product--a,.product--b{top:126px}
  .product--c{top:119px}
  .product h2{font-size:17px;font-weight:800;line-height:21px}
  .product h2 span{font-weight:400}
  .product .gel-line{font-size:17px;font-weight:400;line-height:21px}
  .product .claim{font-size:11.5px;font-weight:400;line-height:16px}
  .product .claim--gap{margin-bottom:5px}
  .product .stack-gap{margin-top:5px}

  .strength{position:absolute;left:336px;top:253px;display:flex;align-items:center;color:var(--white)}
  .strength-num{font-size:25px;font-weight:800;line-height:25px}
  .strength-text{margin-left:6px;font-size:9.6px;font-weight:500;line-height:11px}

  .free-of{position:absolute;left:320px;top:323px;font-size:10.6px;line-height:15.5px;color:var(--white)}
  .label--two .free-of{left:327px}
  .volume{position:absolute;left:474px;top:335px;font-size:18.5px;font-weight:500;color:var(--navy)}
</style>
</head>
<body>

<!-- Label option 1 -->
<section class="label label--one">
  <svg class="label-shapes" viewBox="0 0 548 368" aria-hidden="true">
    <rect x="0" y="0" width="20" height="368" fill="var(--orange)"/>
    <rect x="20" y="0" width="8" height="368" fill="var(--teal)"/>
    <polygon points="20,0 108,0 76,46 20,46" fill="var(--teal)"/>
    <rect x="28" y="252" width="220" height="25" fill="var(--blush)"/>
    <rect x="28" y="277" width="212" height="33" fill="var(--mist)"/>
    <polygon points="248,252 498,252 490,277 240,277" fill="var(--orange)"/>
    <polygon points="20,310 232,310 240,277 490,277 462,368 20,368" fill="var(--navy)"/>
    <polygon points="548,92 548,368 462,368" fill="var(--teal)"/>
  </svg>
  <div class="side-strip"><p><b>BRISKEN</b>&nbsp; Ethanol gel <b>Hand Sanitizer</b> meets <b>Health Canada</b> and the <b>World Health Organization Standards</b></p></div>
  <div class="brand-small">BRISKEN</div>
  <div class="brand-large">BRISKEN</div>

  <h3 class="info-title">HAND SANITIZER <span>Gel</span> / ANTISEPTIQUE POUR LES MAINS <span>Gel</span></h3>
  <div class="info-body">
    <p><b>Drug facts/Info-médicament</b><br><b>Active ingredient/Ingrédients actif:</b> Ethyl alcohol (70%), Alcool éthylique (70 %).<br><b>Inactive ingredients/Ingrédients inactifs:</b> Glycerin, hydroxypropyl methylcellulose stearoxy ether, sodium chloride, acid blue 25, peppermint essential oil, distilled water, citral, dipropylene glycol, linalool, citronellol, coumarin. Glycérine, hydroxypropyl methylcellulose stearoxy ether, chlorure de sodium, bleu acide 25, huile essentielle de menthe poivrée, eau distillée, citral, dipropylene glycol, linalool, citronellol, coumarin.</p>
    <p><b>Purpose/Fin:</b> Antibacterial, antiseptic (skin) cleanser. Nettoyant antibactérien et antiseptique (pour la peau).</p>
    <p><b>Use/Usages:</b> Kills harmful bacteria/germs. Helps prevent spread of bacteria. Tue les bactéries/germes nocifs. Contribue à prévenir la propagation des bactéries.</p>
    <p><b>Dose/Dose:</b><br><b>Children 2 - 11 years/Enfants de 2 à 11 ans</b> — Rub thoroughly into hands for at least 30 seconds. Allow to dry. Supervise children when they use this product. For occasional and personal domestic use.<br><b>Adolescents 12 - 17 years/Adolescents de 12 à 17 ans</b> — Rub thoroughly into hands for at least 30 seconds. Allow to dry. Supervise children when they use this product. For occasional and personal domestic use. Bien frotter pendant au moins 30 secondes. Laisser sécher. Superviser les enfants durant l'utilisation de ce produit. Pour une utilisation occasionnelle pour usage domestique personnel.<br><b>Adults 18 years &amp; older/Adultes 18 ans et plus</b> — Rub thoroughly into hands for at least 30 seconds. Allow to dry. Supervise children when they use this product. For occasional and personal domestic use. Bien frotter pendant au moins 30 secondes. Laisser sécher. Superviser les enfants durant l'utilisation de ce produit. Pour une utilisation occasionnelle pour usage domestique personnel.</p>
    <p><b>Contraindications/Contre-indication(s):</b> Do not use on children/infants less than 2 years of age (unless directed by a doctor/ physician/ health care practitioner/ health care provider/ health care professional). Ne pas utiliser sur les enfants/nourrissons de moins de 2 ans (sauf sur l'avis d'un médecin/ docteur/ praticien de soins de santé/ fournisseur de soins de santé/ professionnel de la santé).</p>
    <p><b>Directions/Mode d'emploi:</b> Put a thumbnail-sized amount on your palm and rub hands together until dry. Mettre une petite quantité de produit dans la paume et se frotter les mains jusqu'à ce qu'elles soient sèches.</p>
  </div>
  <div class="warning">
    <p><b>Warning/Avertissement:</b><br><b>Flammable</b> — keep away from open flame and sources of heat. For external use only. Keep out of reach of children. If swallowed, call a poison control centre or get medical help right away. Stop use and consult health care professional if irritation develops. When using this product avoid contact with eyes. If contact occurs, rinse thoroughly with water.</p>
    <p><b>Inflammable</b> — tenir à l'écart des flammes nues et des sources de chaleur. Pour usage externe seulement. Tenir hors de la portée des enfants. En cas d'ingestion, appeler immédiatement un centre antipoison ou demander immédiatement de l'aide médicale. En cas d'irritation, cesser toute utilisation et consulter un professionnel de la santé. Éviter tout contact avec les yeux lors de l'utilisation. Si le produit entre en contact avec les yeux, rincer soigneusement avec de l'eau.</p>
  </div>
  <div class="barcode-space"></div>
  <div class="maker">Manufactured and Distributed by:</div>

  <div class="product product--a">
    <h2>HAND SANITIZER <span>Gel</span></h2>
    <p class="claim claim--gap">Kills 99.9% of germs</p>
    <h2>ANTISEPTIQUE<br>POUR LES MAINS <span>Gel</span></h2>
    <p class="claim">Tue 99,9% des germes</p>
  </div>
  <div class="strength"><span class="strength-num">70%</span><span class="strength-text">Ethyl Alcohol<br>d'alcool éthylique</span></div>
  <p class="free-of">Perfume and dye free<br>Inodore et sans colorant</p>
  <p class="volume">473ml</p>
</section>

<!-- Label option 2 -->
<section class="label label--two">
  <svg class="label-shapes" viewBox="0 0 548 368" aria-hidden="true">
    <rect x="0" y="0" width="20" height="368" fill="var(--orange)"/>
    <rect x="20" y="0" width="8" height="368" fill="var(--teal)"/>
    <polygon points="20,0 108,0 76,46 20,46" fill="var(--teal)"/>
    <rect x="28" y="252" width="220" height="25" fill="var(--blush)"/>
    <rect x="28" y="277" width="212" height="33" fill="var(--mist)"/>
    <polygon points="248,252 498,252 490,277 240,277" fill="var(--orange)"/>
    <polygon points="20,310 232,310 240,277 490,277 462,368 20,368" fill="var(--navy)"/>
    <polygon points="548,92 548,368 462,368" fill="var(--teal)"/>
  </svg>
  <div class="side-strip"><p><b>BRISKEN</b>&nbsp; Ethanol gel <b>Hand Sanitizer</b> meets <b>Health Canada</b> and the <b>World Health Organization Standards</b></p></div>
  <div class="brand-small">BRISKEN</div>
  <div class="brand-large">BRISKEN</div>

  <h3 class="info-title">HAND SANITIZER <span>Gel</span> / ANTISEPTIQUE POUR LES MAINS <span>Gel</span></h3>
  <div class="info-body">
    <p><b>Drug facts/Info-médicament</b><br><b>Active ingredient/Ingrédients actif:</b> Ethyl alcohol (70%), Alcool éthylique (70 %).<br><b>Inactive ingredients/Ingrédients inactifs:</b> Glycerin, hydroxypropyl methylcellulose stearoxy ether, sodium chloride, acid blue 25, peppermint essential oil, distilled water, citral, dipropylene glycol, linalool, citronellol, coumarin. Glycérine, hydroxypropyl methylcellulose stearoxy ether, chlorure de sodium, bleu acide 25, huile essentielle de menthe poivrée, eau distillée, citral, dipropylene glycol, linalool, citronellol, coumarin.</p>
    <p><b>Purpose/Fin:</b> Antibacterial, antiseptic (skin) cleanser. Nettoyant antibactérien et antiseptique (pour la peau).</p>
    <p><b>Use/Usages:</b> Kills harmful bacteria/germs. Helps prevent spread of bacteria. Tue les bactéries/germes nocifs. Contribue à prévenir la propagation des bactéries.</p>
    <p><b>Dose/Dose:</b><br><b>Children 2 - 11 years/Enfants de 2 à 11 ans</b> — Rub thoroughly into hands for at least 30 seconds. Allow to dry. Supervise children when they use this product. For occasional and personal domestic use.<br><b>Adolescents 12 - 17 years/Adolescents de 12 à 17 ans</b> — Rub thoroughly into hands for at least 30 seconds. Allow to dry. Supervise children when they use this product. For occasional and personal domestic use. Bien frotter pendant au moins 30 secondes. Laisser sécher. Superviser les enfants durant l'utilisation de ce produit. Pour une utilisation occasionnelle pour usage domestique personnel.<br><b>Adults 18 years &amp; older/Adultes 18 ans et plus</b> — Rub thoroughly into hands for at least 30 seconds. Allow to dry. Supervise children when they use this product. For occasional and personal domestic use. Bien frotter pendant au moins 30 secondes. Laisser sécher. Superviser les enfants durant l'utilisation de ce produit. Pour une utilisation occasionnelle pour usage domestique personnel.</p>
    <p><b>Contraindications/Contre-indication(s):</b> Do not use on children/infants less than 2 years of age (unless directed by a doctor/ physician/ health care practitioner/ health care provider/ health care professional). Ne pas utiliser sur les enfants/nourrissons de moins de 2 ans (sauf sur l'avis d'un médecin/ docteur/ praticien de soins de santé/ fournisseur de soins de santé/ professionnel de la santé).</p>
    <p><b>Directions/Mode d'emploi:</b> Put a thumbnail-sized amount on your palm and rub hands together until dry. Mettre une petite quantité de produit dans la paume et se frotter les mains jusqu'à ce qu'elles soient sèches.</p>
  </div>
  <div class="warning">
    <p><b>Warning/Avertissement:</b><br><b>Flammable</b> — keep away from open flame and sources of heat. For external use only. Keep out of reach of children. If swallowed, call a poison control centre or get medical help right away. Stop use and consult health care professional if irritation develops. When using this product avoid contact with eyes. If contact occurs, rinse thoroughly with water.</p>
    <p><b>Inflammable</b> — tenir à l'écart des flammes nues et des sources de chaleur. Pour usage externe seulement. Tenir hors de la portée des enfants. En cas d'ingestion, appeler immédiatement un centre antipoison ou demander immédiatement de l'aide médicale. En cas d'irritation, cesser toute utilisation et consulter un professionnel de la santé. Éviter tout contact avec les yeux lors de l'utilisation. Si le produit entre en contact avec les yeux, rincer soigneusement avec de l'eau.</p>
  </div>
  <div class="barcode-space"></div>
  <div class="maker">Manufactured and Distributed by:</div>

  <div class="product product--b">
    <h2>HAND SANITIZER <span>Gel</span></h2>
    <h2 class="stack-gap">ANTISEPTIQUE<br>POUR LES MAINS <span>Gel</span></h2>
    <p class="claim stack-gap">Kills 99.9% of germs</p>
    <p class="claim">Tue 99,9% des germes</p>
  </div>
  <div class="strength"><span class="strength-num">70%</span><span class="strength-text">Ethyl Alcohol<br>d'alcool éthylique</span></div>
  <p class="free-of">Perfume and dye free<br>Inodore et sans colorant</p>
  <p class="volume">473ml</p>
</section>

<!-- Label option 3 -->
<section class="label label--three">
  <svg class="label-shapes" viewBox="0 0 548 368" aria-hidden="true">
    <rect x="0" y="0" width="20" height="368" fill="var(--orange)"/>
    <rect x="20" y="0" width="8" height="368" fill="var(--teal)"/>
    <polygon points="20,0 108,0 76,46 20,46" fill="var(--teal)"/>
    <rect x="28" y="252" width="220" height="25" fill="var(--blush)"/>
    <rect x="28" y="277" width="212" height="33" fill="var(--mist)"/>
    <polygon points="248,252 498,252 490,277 240,277" fill="var(--orange)"/>
    <polygon points="20,310 232,310 240,277 490,277 462,368 20,368" fill="var(--navy)"/>
    <polygon points="548,92 548,368 462,368" fill="var(--teal)"/>
  </svg>
  <div class="side-strip"><p><b>BRISKEN</b>&nbsp; Ethanol gel <b>Hand Sanitizer</b> meets <b>Health Canada</b> and the <b>World Health Organization Standards</b></p></div>
  <div class="brand-small">BRISKEN</div>
  <div class="brand-large">BRISKEN</div>

  <h3 class="info-title">HAND SANITIZER <span>Gel</span> / ANTISEPTIQUE POUR LES MAINS <span>Gel</span></h3>
  <div class="info-body">
    <p><b>Drug facts/Info-médicament</b><br><b>Active ingredient/Ingrédients actif:</b> Ethyl alcohol (70%), Alcool éthylique (70 %).<br><b>Inactive ingredients/Ingrédients inactifs:</b> Glycerin, hydroxypropyl methylcellulose stearoxy ether, sodium chloride, acid blue 25, peppermint essential oil, distilled water, citral, dipropylene glycol, linalool, citronellol, coumarin. Glycérine, hydroxypropyl methylcellulose stearoxy ether, chlorure de sodium, bleu acide 25, huile essentielle de menthe poivrée, eau distillée, citral, dipropylene glycol, linalool, citronellol, coumarin.</p>
    <p><b>Purpose/Fin:</b> Antibacterial, antiseptic (skin) cleanser. Nettoyant antibactérien et antiseptique (pour la peau).</p>
    <p><b>Use/Usages:</b> Kills harmful bacteria/germs. Helps prevent spread of bacteria. Tue les bactéries/germes nocifs. Contribue à prévenir la propagation des bactéries.</p>
    <p><b>Dose/Dose:</b><br><b>Children 2 - 11 years/Enfants de 2 à 11 ans</b> — Rub thoroughly into hands for at least 30 seconds. Allow to dry. Supervise children when they use this product. For occasional and personal domestic use.<br><b>Adolescents 12 - 17 years/Adolescents de 12 à 17 ans</b> — Rub thoroughly into hands for at least 30 seconds. Allow to dry. Supervise children when they use this product. For occasional and personal domestic use. Bien frotter pendant au moins 30 secondes. Laisser sécher. Superviser les enfants durant l'utilisation de ce produit. Pour une utilisation occasionnelle pour usage domestique personnel.<br><b>Adults 18 years &amp; older/Adultes 18 ans et plus</b> — Rub thoroughly into hands for at least 30 seconds. Allow to dry. Supervise children when they use this product. For occasional and personal domestic use. Bien frotter pendant au moins 30 secondes. Laisser sécher. Superviser les enfants durant l'utilisation de ce produit. Pour une utilisation occasionnelle pour usage domestique personnel.</p>
    <p><b>Contraindications/Contre-indication(s):</b> Do not use on children/infants less than 2 years of age (unless directed by a doctor/ physician/ health care practitioner/ health care provider/ health care professional). Ne pas utiliser sur les enfants/nourrissons de moins de 2 ans (sauf sur l'avis d'un médecin/ docteur/ praticien de soins de santé/ fournisseur de soins de santé/ professionnel de la santé).</p>
    <p><b>Directions/Mode d'emploi:</b> Put a thumbnail-sized amount on your palm and rub hands together until dry. Mettre une petite quantité de produit dans la paume et se frotter les mains jusqu'à ce qu'elles soient sèches.</p>
  </div>
  <div class="warning">
    <p><b>Warning/Avertissement:</b><br><b>Flammable</b> — keep away from open flame and sources of heat. For external use only. Keep out of reach of children. If swallowed, call a poison control centre or get medical help right away. Stop use and consult health care professional if irritation develops. When using this product avoid contact with eyes. If contact occurs, rinse thoroughly with water.</p>
    <p><b>Inflammable</b> — tenir à l'écart des flammes nues et des sources de chaleur. Pour usage externe seulement. Tenir hors de la portée des enfants. En cas d'ingestion, appeler immédiatement un centre antipoison ou demander immédiatement de l'aide médicale. En cas d'irritation, cesser toute utilisation et consulter un professionnel de la santé. Éviter tout contact avec les yeux lors de l'utilisation. Si le produit entre en contact avec les yeux, rincer soigneusement avec de l'eau.</p>
  </div>
  <div class="barcode-space"></div>
  <div class="maker">Manufactured and Distributed by:</div>

  <div class="product product--c">
    <h2>HAND SANITIZER</h2>
    <h2 class="stack-gap">ANTISEPTIQUE<br>POUR LES MAINS</h2>
    <p class="gel-line">Gel</p>
    <p class="claim">Kills 99.9% of germs</p>
    <p class="claim">Tue 99,9% des germes</p>
  </div>
  <div class="strength"><span class="strength-num">70%</span><span class="strength-text">Ethyl Alcohol<br>d'alcool éthylique</span></div>
  <p class="free-of">Perfume and dye free<br>Inodore et sans colorant</p>
  <p class="volume">473ml</p>
</section>

</body>
</html>
```